4D Hush Little Nest Luxury Ultrasound Billboard

Design a HIGH-END, MODERN billboard for my private prenatal ultrasound studio, 4D Hush Little Nest, located in Pace, Florida.
This billboard will be viewed by drivers traveling at highway speeds, so it must be extremely clean, simple, and readable within 6 seconds.
About My Business
4D Hush Little Nest is a private prenatal ultrasound studio specializing in:
Highest technology 4D/HD Ultrasounds
Early Gender Determination
Pregnancy Confirmation
I have been serving families for nearly 10 years and is known for creating a memorable experience, not just an ultrasound appointment.
Design Style
I DO NOT want:
Flowers
Leaves
Swirls
Glitter
Hearts everywhere
Busy backgrounds
Generic maternity stock graphics
I DO want:
Modern
Luxury
Upscale
Clean
Professional
Eye-catching
Premium medical spa feel
Colors
Use colors from my logo:
LOGO Green ( or a deep green)
Black
White
Soft Gold accents
Images:
Incorporate my professional headshot in a clean, modern way, logo, and the ultrasound images
Text
Keep wording minimal.
Primary Headline ( OPEN TO IDEAS) :
EXAMPLES ( WOULD RATHER SOMETHING MORE CATCHY)
" ADVANCED IMAGING. UNFORGETTABLE MOMENTS"
"MEET YOUR BABY BEFORE BIRTH"
Under headline:
4D Ultrasound • Early Gender • Pregnancy Confirmation
Business Name:
4D Hush Little Nest
Private Prenatal Ultrasound Studio
Phone Number:
850-471-3905
Important
This billboard must be readable in 5–6 seconds from a moving vehicle.
Less text is better.
The phone number and business name must be visible from a distance.
The design should feel like a premium brand that immediately tells expecting parents:
“This is where I go to see my baby.”
Files Provided
Official logo
Headshot
Ultrasound images
Don’t make this look like a medical office billboard.
Make it look like a luxury baby experience billboard. That’s what separates 4D Hush Little Nest from hospitals, OB offices, and all the new studios popping up around you. The emotional connection is what gets moms to book. ❤️
Billboard Size - 10.6” x 36”

```html
<!DOCTYPE html>
<html lang="en">
<head>
<meta charset="utf-8">
<title>4D Hush Little Nest – Billboard</title>
<link href="https://fonts.googleapis.com/css2?family=Montserrat:wght@800&family=Poppins:wght@500;600;700&display=swap" rel="stylesheet">
<style>
  :root {
    --ink: #000000;
    --paper: #ffffff;
    --page: #f2f2f0;
    --gold-light: #f3dc8e;
    --gold: #d4ab5c;
    --gold-deep: #b8893f;
    --green: #1f4a2c;
    --skin: #d9b9a0;
    --scan-dark: #3a1a12;
    --scan: #a65a44;
  }
  * { box-sizing: border-box; margin: 0; padding: 0; }
  html, body {
    width: 1200px; height: 1046px; overflow: hidden;
    background: var(--page);
  }
  .billboard {
    position: absolute; left: 30px; top: 355px;
    width: 1140px; height: 336px;
    background: var(--ink); overflow: hidden;
    font-family: "Poppins", sans-serif;
  }
  .billboard__swoosh { position: absolute; inset: 0; }
  .headshot {
    position: absolute; left: 0; top: 0; width: 196px; height: 336px;
    background: linear-gradient(180deg, #cdb08a 0%, var(--skin) 38%, var(--green) 70%, #173a22 100%);
  }
  .headline {
    position: absolute; left: 220px; font-family: "Montserrat", sans-serif; font-weight: 800;
    line-height: 1; letter-spacing: -0.5px;
    background: linear-gradient(90deg, var(--gold-light) 0%, var(--gold) 45%, var(--gold-deep) 100%);
    -webkit-background-clip: text; background-clip: text; color: transparent;
  }
  .headline--main { top: 20px; font-size: 70px; }
  .headline--sub { top: 96px; font-size: 50px; }
  .services { position: absolute; left: 222px; top: 172px; list-style: none; }
  .services__item {
    display: flex; align-items: center; gap: 10px; height: 30px;
    color: var(--paper); font-weight: 500; font-size: 19px;
  }
  .services__tick { width: 20px; height: 20px; flex: none; }
  .phone {
    position: absolute; left: 218px; top: 268px;
    color: var(--paper); font-weight: 700; font-size: 46px; line-height: 1; letter-spacing: 0.5px;
  }
  .brand-name {
    position: absolute; left: 650px; top: 128px; width: 180px; text-align: center;
    color: var(--gold); font-weight: 600; font-size: 26px; line-height: 1.15;
  }
  .scan {
    position: absolute; left: 866px; top: 90px; width: 194px; height: 194px;
    border-radius: 50%; border: 4px solid var(--gold);
    background: radial-gradient(circle at 50% 45%, var(--scan) 0%, #7e3b2b 55%, var(--scan-dark) 100%);
  }
  .website {
    position: absolute; right: 22px; top: 290px;
    color: var(--ink); font-weight: 700; font-size: 31px; line-height: 1;
  }
</style>
</head>
<body>
  <section class="billboard">
    <svg class="billboard__swoosh" viewBox="0 0 1140 336" width="1140" height="336" aria-hidden="true">
      <path d="M 574 336 C 660 268, 790 224, 922 224 L 1050 232 C 1106 214, 1134 150, 1140 80 L 1140 336 Z" fill="#d4ab5c"/>
      <path d="M 640 336 C 720 272, 820 236, 930 236 L 1050 244 C 1110 226, 1136 170, 1140 108 L 1140 336 Z" fill="#ffffff"/>
    </svg>

    <div class="headshot" role="img" aria-label="Professional headshot of the studio owner holding an ultrasound probe"></div>

    <h1 class="headline headline--main">MEET YOUR BABY</h1>
    <p class="headline headline--sub">BEFORE BIRTH</p>

    <ul class="services">
      <li class="services__item">
        <svg class="services__tick" viewBox="0 0 20 20"><rect x="1.5" y="3.5" width="15" height="15" rx="3" fill="none" stroke="#d4ab5c" stroke-width="2.2"/><path d="M5 10.5 L9 14.5 L18 3" fill="none" stroke="#d4ab5c" stroke-width="3" stroke-linecap="round" stroke-linejoin="round"/></svg>
        4D Ultrasound
      </li>
      <li class="services__item">
        <svg class="services__tick" viewBox="0 0 20 20"><rect x="1.5" y="3.5" width="15" height="15" rx="3" fill="none" stroke="#d4ab5c" stroke-width="2.2"/><path d="M5 10.5 L9 14.5 L18 3" fill="none" stroke="#d4ab5c" stroke-width="3" stroke-linecap="round" stroke-linejoin="round"/></svg>
        Pregnancy Confirmation
      </li>
      <li class="services__item">
        <svg class="services__tick" viewBox="0 0 20 20"><rect x="1.5" y="3.5" width="15" height="15" rx="3" fill="none" stroke="#d4ab5c" stroke-width="2.2"/><path d="M5 10.5 L9 14.5 L18 3" fill="none" stroke="#d4ab5c" stroke-width="3" stroke-linecap="round" stroke-linejoin="round"/></svg>
        Early Gender
      </li>
    </ul>

    <p class="phone">850·471·3905</p>

    <p class="brand-name">4D Hush<br>Little Nest</p>

    <div class="scan" role="img" aria-label="Circular 4D ultrasound image of twin babies"></div>

    <p class="website">4DHushLittleNest.com</p>
  </section>
</body>
</html>
```